Business Card Design

We need business cards designed incorporating our graphics/logo already used on our trucks. We are a small construction company that does everything from building new homes, additions, Kitchens, Baths, Decks, Hardwood Floors/Tile, all phases of construction. No job is too small. We pride ourselves on True Craftmanship/Customer Satisfaction, its what truly separates us from everyone else.

Industry/Entity Type

Construction

Contact Information for Business Card

Maple Ridge Renovations Lic#27KP51986400
342 51st Avenue Harbor Point NJ 07391
(555)731-2948 Email: info@mapleridgeexample.com
Paul Vandermolen

```html
<!DOCTYPE html>
<html lang="en">
<head>
<meta charset="utf-8">
<title>Maple Ridge Renovations – Business Cards</title>
<link href="https://fonts.googleapis.com/css2?family=Roboto:wght@400;700;900&display=swap" rel="stylesheet">
<style>
  :root {
    --page-bg: #e9e6e1;
    --sky-light: #eaf5fb;
    --sky-deep: #8ec6e3;
    --sand-light: #ecd8b4;
    --sand-deep: #c9a676;
    --ink: #1a1a1a;
    --ribbon: #111111;
    --paper-white: #ffffff;
    --title-tone: #b8935a;
    --muted: #6d747a;
    --art-workers: #7f86b8;
    --art-plane: #c9524a;
  }
  * { box-sizing: border-box; margin: 0; padding: 0; }
  html, body { width: 1200px; height: 1023px; overflow: hidden; }
  body {
    background: var(--page-bg);
    font-family: "Roboto", Arial, sans-serif;
    color: var(--ink);
    position: relative;
  }
  .card {
    position: absolute;
    left: 180px;
    width: 840px;
    height: 480px;
    overflow: hidden;
    box-shadow: 0 6px 18px rgba(0,0,0,.18);
  }
  .card--front { top: 20px; background: linear-gradient(180deg, var(--sky-light) 0%, var(--sky-deep) 70%); }
  .card--back  { top: 523px; background: linear-gradient(135deg, var(--sand-light) 0%, var(--sand-deep) 100%); }

  .sand-ground { position: absolute; inset: 0; width: 840px; height: 480px; }

  .art { position: absolute; border-radius: 6px; }
  .art--workers { background: radial-gradient(ellipse at 50% 55%, var(--art-workers) 0%, #b7bcd8 60%, rgba(183,188,216,0) 100%); }
  .art--plane { background: linear-gradient(90deg, var(--art-plane), #e3908a); border-radius: 10px; }

  .brand-title {
    position: absolute;
    font-weight: 900;
    text-transform: uppercase;
    line-height: 1.05;
  }
  .card--front .brand-title {
    left: 330px; top: 22px; width: 470px;
    font-size: 46px; text-align: center; color: var(--title-tone);
  }
  .card--back .brand-title {
    left: 450px; top: 222px; width: 240px;
    font-size: 32px; text-align: left; color: var(--ink);
  }

  .license { position: absolute; left: 30px; top: 198px; font-size: 15px; color: var(--muted); }

  .contact-name { position: absolute; left: 470px; top: 250px; font-size: 28px; font-weight: 700; text-transform: uppercase; }

  .ribbon { position: absolute; }
  .ribbon__text {
    position: absolute; inset: 0;
    display: flex; align-items: center; justify-content: center;
    color: var(--paper-white); font-weight: 700; letter-spacing: 2px;
  }
  .card--front .ribbon { left: 440px; top: 295px; width: 300px; height: 52px; }
  .card--front .ribbon__text { font-size: 26px; padding-left: 14px; }
  .card--back .ribbon { left: 420px; top: 58px; width: 390px; height: 78px; }
  .card--back .ribbon__text { font-size: 36px; padding-left: 30px; }

  .contact-email { position: absolute; left: 470px; top: 368px; font-size: 20px; }
  .contact-address { position: absolute; left: 380px; top: 410px; font-size: 20px; line-height: 1.3; text-transform: uppercase; }

  .services {
    position: absolute; left: 450px; top: 335px;
    list-style: none; color: var(--paper-white);
    font-weight: 700; font-size: 22px; text-transform: uppercase; line-height: 1.5;
  }
  .services li::before {
    content: ""; display: inline-block; width: 9px; height: 9px;
    border-radius: 50%; background: var(--ink); margin-right: 12px; vertical-align: middle;
  }
</style>
</head>
<body>

  <section class="card card--front">
    <svg class="sand-ground" viewBox="0 0 840 480" aria-hidden="true">
      <defs>
        <linearGradient id="sandFront" x1="0" y1="0" x2="1" y2="1">
          <stop offset="0" stop-color="#ecd8b4"/>
          <stop offset="1" stop-color="#c9a676"/>
        </linearGradient>
      </defs>
      <path d="M300,480 C320,430 300,390 340,345 C380,300 420,300 445,250 C475,200 620,225 840,165 L840,480 Z"
            fill="url(#sandFront)" stroke="#3a2e20" stroke-width="2"/>
    </svg>

    <h1 class="brand-title">Maple<br>Ridge<br>Renovations</h1>
    <p class="license">Lic#27KP51986400</p>

    <div class="art art--workers" role="img" aria-label="Illustration of two smiling builders in hard hats beside a signpost" style="left:20px; top:222px; width:280px; height:250px;"></div>
    <div class="art art--plane" role="img" aria-label="Illustration of a small red biplane towing the phone banner" style="left:715px; top:195px; width:100px; height:50px;"></div>

    <p class="contact-name">Paul Vandermolen</p>
    <div class="ribbon">
      <svg viewBox="0 0 300 52" width="300" height="52" aria-hidden="true">
        <path d="M0,6 L300,0 L300,46 L8,52 L20,28 Z" fill="var(--ribbon)"/>
      </svg>
      <span class="ribbon__text">(555) 731 - 2948</span>
    </div>
    <p class="contact-email">info@mapleridgeexample.com</p>
    <p class="contact-address">342 51st Avenue<br>Harbor Point NJ 07391</p>
  </section>

  <section class="card card--back">
    <div class="art art--workers" role="img" aria-label="Illustration of two smiling builders in hard hats beside a signpost" style="left:40px; top:40px; width:360px; height:400px;"></div>

    <div class="ribbon">
      <svg viewBox="0 0 390 78" width="390" height="78" aria-hidden="true">
        <path d="M0,0 L28,8 L390,12 L390,78 L20,70 L36,36 Z" fill="var(--ribbon)"/>
      </svg>
      <span class="ribbon__text">(555) 731 - 2948</span>
    </div>
    <div class="art art--plane" role="img" aria-label="Illustration of a small red biplane towing the phone banner" style="left:705px; top:160px; width:105px; height:60px;"></div>

    <h2 class="brand-title">Maple Ridge<br>Renovations</h2>
    <ul class="services">
      <li>Remodeling</li>
      <li>Decks</li>
      <li>Additions</li>
    </ul>
  </section>

</body>
</html>
```